Real estate Agent postcards for homeowners

I need a "Just Sold" postcard for two real agents , I am providing pictures of the agents and neighborhood.
I have the front and back of a postcard containing the information I want on the postcard.
I want a designer to take the info and pictures and design a new postcard and choose the colors

Target Market(s)

homeowners of luxury condos

Industry/Entity Type

Real Estate Agent

Colors

Designer to choose colors to be used in the design.

```html
<!DOCTYPE html>
<html lang="en">
<head>
<meta charset="utf-8">
<title>Harbor Crest Realty – Postcard</title>
<link rel="stylesheet" href="https://fonts.googleapis.com/css2?family=Fira+Sans:wght@300;400;500;600;700&display=swap">
<style>
  :root{
    --gold-light:#e3cc86;
    --gold:#c7a865;
    --gold-dark:#a8864a;
    --gold-text:#d8b56a;
    --blue-deep:#154a86;
    --blue-mid:#2a6ca8;
    --blue-glow:#7ab8dc;
    --navy:#17406f;
    --white:#ffffff;
    --ink:#111111;
  }
  html,body{margin:0;padding:0;overflow:hidden;background:var(--white);}
  .postcard{
    position:relative;width:1200px;height:857px;overflow:hidden;
    font-family:"Fira Sans",sans-serif;color:var(--white);background:var(--white);
  }
  .front-panel{position:absolute;left:0;top:0;width:600px;height:744px;
    background:radial-gradient(ellipse 300px 260px at 590px 250px,var(--blue-glow) 0%,rgba(122,184,220,0) 100%),
      linear-gradient(180deg,#1f5e9c 0%,var(--blue-mid) 40%,var(--blue-deep) 100%);}
  .hero-photo{position:absolute;left:0;top:480px;width:600px;height:264px;
    background:linear-gradient(180deg,rgba(21,74,134,0) 0%,rgba(16,52,96,.75) 45%,#0f3a6c 100%);}
  .header-band{position:absolute;left:0;top:0;width:600px;height:94px;
    background:linear-gradient(90deg,var(--gold-dark) 0%,var(--gold) 50%,var(--gold-light) 100%);
    border-bottom:4px solid #b08c48;}
  .brand-title{position:absolute;right:20px;top:48px;margin:0;font-size:45px;font-weight:700;letter-spacing:.5px;line-height:1;}
  .tagline{position:absolute;right:26px;top:118px;margin:0;text-align:right;font-size:24px;font-weight:300;line-height:30px;}
  .agent{position:absolute;}
  .agent-icon{position:absolute;left:-32px;top:-2px;width:31px;height:31px;}
  .agent-name{margin:0;font-size:27px;font-weight:600;line-height:28px;}
  .agent-rule{width:234px;border-top:2px dotted rgba(255,255,255,.75);margin-top:10px;}
  .agent-phone{margin:14px 0 0;font-size:30px;font-weight:300;line-height:32px;}
  .agent-email{margin:2px 0 0;font-size:20px;font-weight:400;line-height:24px;}
  .agent-one{left:76px;top:279px;}
  .agent-two{left:321px;top:421px;}
  .web-cta{position:absolute;left:130px;width:482px;top:653px;text-align:center;}
  .web-cta-lead{margin:0;font-size:19px;font-weight:400;}
  .web-cta-url{margin:6px 0 0;font-size:30px;font-weight:600;}
  .footer-shapes{position:absolute;left:0;top:0;}
  .footer-name{position:absolute;left:42px;top:754px;margin:0;font-size:30px;font-weight:500;}
  .footer-address{position:absolute;left:42px;top:805px;margin:0;font-size:21px;font-weight:400;color:var(--gold-text);}
  .listing-badge{position:absolute;left:652px;top:712px;}
  .license{position:absolute;left:780px;top:745px;margin:0;font-size:20px;font-weight:500;color:var(--ink);}
  .disclaimer{position:absolute;left:690px;width:460px;top:786px;margin:0;text-align:center;font-size:16px;font-weight:300;line-height:21px;}
</style>
</head>
<body>
<div class="postcard">
  <section class="front-panel">
    <div class="hero-photo" role="img" aria-label="Luxury home with lit windows and pool at dusk"></div>
    <header class="header-band"><h1 class="brand-title">HARBOR CREST REALTY</h1></header>
    <p class="tagline">We are Bayview agents and<br>your Seabrook Cove neighbors.<br>Call us for a free property market evaluation.</p>

    <div class="agent agent-one">
      <svg class="agent-icon" viewBox="0 0 32 32"><circle cx="16" cy="16" r="14" fill="none" stroke="#d8b56a" stroke-width="2.5"/><path d="M12 9 L23 16 L12 23 Z" fill="#e3cc86"/></svg>
      <h2 class="agent-name">MARLA QUINLAN</h2>
      <div class="agent-rule"></div>
      <p class="agent-phone">(310) 555-0148</p>
      <p class="agent-email">HomesbyMarla@example.com</p>
    </div>

    <div class="agent agent-two">
      <svg class="agent-icon" viewBox="0 0 32 32"><circle cx="16" cy="16" r="14" fill="none" stroke="#d8b56a" stroke-width="2.5"/><path d="M12 9 L23 16 L12 23 Z" fill="#e3cc86"/></svg>
      <h2 class="agent-name">THEO VARKAS</h2>
      <div class="agent-rule"></div>
      <p class="agent-phone">(650) 555-0192</p>
      <p class="agent-email">TheoVarkas@example.com</p>
    </div>

    <div class="web-cta">
      <p class="web-cta-lead">For more details, Visit Us at</p>
      <p class="web-cta-url">www.HarborCrestRealty.com</p>
    </div>
  </section>

  <svg class="footer-shapes" width="1200" height="857" viewBox="0 0 1200 857">
    <defs>
      <linearGradient id="goldBand" x1="0" x2="1" y1="0" y2="0">
        <stop offset="0" stop-color="#9c7c44"/><stop offset=".5" stop-color="#b89858"/><stop offset="1" stop-color="#d2b574"/>
      </linearGradient>
      <linearGradient id="edgeShade" x1="0" x2="1" y1="0" y2="0">
        <stop offset="0" stop-color="#000" stop-opacity=".18"/><stop offset="1" stop-color="#000" stop-opacity="0"/>
      </linearGradient>
    </defs>
    <polygon points="600,744 684,857 720,857 630,744" fill="url(#edgeShade)"/>
    <polygon points="628,777 1200,777 1200,857 684,857" fill="url(#goldBand)"/>
    <polygon points="0,744 600,744 684,857 0,857" fill="var(--navy)"/>
    <polyline points="0,744 600,744 684,857" fill="none" stroke="#ffffff" stroke-width="2"/>
  </svg>

  <p class="footer-name">HARBOR CREST REALTY</p>
  <p class="footer-address">415, Shoreline Ave, BAYVIEW, CA 90000-1234</p>

  <svg class="listing-badge" width="108" height="56" viewBox="0 0 108 56">
    <rect x="1" y="1" width="106" height="54" fill="#fff" stroke="#111" stroke-width="1.5"/>
    <rect x="6" y="6" width="38" height="36" fill="#111"/>
    <rect x="52" y="24" width="50" height="20" fill="#111"/>
  </svg>
  <p class="license">CALBRE # 01234567</p>
  <p class="disclaimer">If your property is already listed with a broker,<br>please disregard tis mailing.<br>This is not a solicitation.</p>
</div>
</body>
</html>
```